Re-design of veterinary clinic website *

For a future relaunch of our webpage, we would like to find a fresh design that still incorporates the spirit of our current one which can be found at http://dr-wenzlaff.de
We are a small business that appeals to locals but are known in a wide area for specialist services.
According to analytics data, most people rarely read through the full website but are using it to inform themselves about opening hours, Telephone numbers and location. Still, the website needs to offer enough content to be ranked positively by the Quandle algorithm.
Our logo is not part of the re-design but needs to be included in your proposal as is. It can be used a source of inspiration, just as the current design. Keep in mind, that the design will be used as the basis of a fluid webdesign for both mobile and desktop. Roughly 75% of our users are on mobile devices.
Target Market(s)
Locals
Industry/Entity Type
Veterinary
Number of Pages Required
1 page
Look and feel
Each slider illustrates characteristics of the customer's brand and the style your logo design should communicate.

```html
<!DOCTYPE html>
<html lang="de">
<head>
<meta charset="utf-8">
<title>Dr. med. vet. Jonas Wenzlaff – Tierarztpraxis</title>
<link href="https://fonts.googleapis.com/css2?family=Nunito+Sans:wght@400;600;700;800&display=swap" rel="stylesheet">
<style>
:root{
  --blue:#0a4fa0;
  --navy:#12357a;
  --sky:#8ac8e6;
  --ink:#1d1d24;
  --text:#333;
  --white:#fff;
  --fur:#a86a3a;
  --fur-dark:#6e4024;
  --mint:#cfe6df;
}
*{box-sizing:border-box;margin:0;padding:0}
html,body{width:1200px;height:3005px;overflow:hidden}
body{position:relative;background:var(--white);font-family:"Nunito Sans",sans-serif;color:var(--ink)}
.abs{position:absolute}
.header{left:0;top:0;width:1200px;height:112px;background:#fafbfc}
.brand{left:0;width:1200px;top:40px;display:flex;justify-content:center;align-items:center;gap:14px}
.brand-name{font-size:24px;font-weight:700;color:var(--blue);letter-spacing:3px}
.brand-dot{width:26px;height:26px;border:2px solid var(--blue);border-radius:50%}
.nav{left:0;top:112px;width:1200px;height:46px;background:var(--blue);display:flex;justify-content:center;align-items:center;gap:44px}
.nav a{color:var(--white);text-decoration:none;font-size:13px;font-weight:800;letter-spacing:1px}

.hero{left:0;top:158px;width:1200px;height:507px;
  background:
    linear-gradient(180deg,rgba(255,255,255,0) 60%,rgba(214,140,96,.35) 100%),
    linear-gradient(90deg,var(--fur-dark) 0%,var(--fur) 22%,#c9955f 40%,#e6ddd0 58%,var(--mint) 78%,#e9f2ef 100%)}

.welcome-kicker{left:90px;top:748px;font-size:16px}
.welcome-title{left:90px;top:780px;font-size:23px;font-weight:600;color:var(--navy)}
.welcome-text{left:90px;top:820px;width:560px;font-size:15px;line-height:19.5px;color:var(--text);letter-spacing:.2px}
.pets-photo{left:690px;top:690px;width:420px;height:310px;border-radius:6px;
  background:linear-gradient(90deg,#f4f4f4 0%,#5d5f63 18%,#e3a35f 42%,#f0c48f 52%,#4b3a2c 72%,#a37a4e 86%,#f4f4f4 100%)}

.praxis-back{left:438px;top:1066px;width:762px;height:404px;background:var(--blue)}
.praxis-panel{left:92px;top:1090px;width:1012px;height:352px;background:var(--sky)}
.praxis-photo{border:2px solid var(--white)}
.praxis-photo.one{left:144px;top:1134px;width:258px;height:194px;background:linear-gradient(180deg,#8db07a 0%,#c8d3c0 45%,#d9d9d4 70%,#9aa0a5 100%)}
.praxis-photo.two{left:330px;top:1202px;width:258px;height:196px;background:linear-gradient(180deg,#d4d8dc 0%,#eef0ec 45%,#c8ccc9 75%,#8f9691 100%)}
.praxis-label{left:646px;top:1168px;font-size:16px}
.praxis-text{left:646px;top:1200px;width:436px;font-size:24px;line-height:30px;font-weight:600;color:#12264f}
.praxis-text .year{color:var(--blue)}
.read-more{z-index:2;font-size:13px;font-weight:800;color:var(--ink);text-decoration:none;border-bottom:2px solid var(--ink);padding-bottom:1px}

.team-title{left:182px;top:1526px;font-size:17px;font-weight:700;color:var(--navy)}
.team-text{left:182px;top:1562px;width:556px;font-size:17px;line-height:26.5px;font-weight:600;z-index:2}
.portrait{top:1552px;width:116px;height:120px}
.portrait.a{left:826px;background:linear-gradient(180deg,#c6d0d8 0%,#b69680 55%,#8c7466 100%)}
.portrait.b{left:952px;background:linear-gradient(180deg,#b3bec3 0%,#7a5a48 55%,#4a3228 100%)}

.services-bg{left:0;top:1700px;width:1200px;height:520px;background:linear-gradient(90deg,#f1f2f5 0%,#f6f7f9 45%,#fff 75%)}
.services-photo{left:90px;top:1780px;width:520px;height:420px;
  background:linear-gradient(180deg,#f3f3f3 0%,#e9e6e3 15%,#9a5a33 40%,#7a3e1f 58%,#2b2b2e 75%,#f1f1f1 100%)}
.services-title{left:610px;top:1848px;font-size:31px;font-weight:600}
.service{font-size:12px;font-weight:600;letter-spacing:1.5px}
.btn{background:var(--blue);color:var(--white);font-size:13px;font-weight:800;display:flex;align-items:center;justify-content:center;text-decoration:none}

.map{left:92px;top:2238px;width:576px;height:356px;background:#e8e6df;border:1px solid #d5d3cc}
.vet-photo{left:668px;top:2238px;width:436px;height:356px;
  background:linear-gradient(90deg,#e6ecf0 0%,#f4f4f2 30%,#b59c84 55%,#8d7664 70%,#ece6e0 100%)}

.contact-name{left:96px;top:2646px;font-size:20px;font-weight:700;color:var(--navy)}
.contact-line{left:96px;font-size:17px;font-weight:700;letter-spacing:.5px}
.hours-title{left:632px;top:2636px;font-size:18px;font-weight:800;color:var(--navy);padding-bottom:6px;border-bottom:2px solid var(--navy);width:394px}
.hours{left:632px;top:2686px;border-collapse:collapse;font-size:15px}
.hours td{height:31px;padding:0}
.hours td:nth-child(1){width:144px}
.hours td:nth-child(2){width:156px}
.footer{left:0;top:2950px;width:1200px;height:55px;background:var(--sky);display:flex;align-items:center;justify-content:center;font-size:12px;font-weight:800;letter-spacing:1.5px;color:var(--navy)}
</style>
</head>
<body>
<header class="abs header">
  <div class="abs brand"><span class="brand-dot"></span><span class="brand-name">Dr. med. vet. Jonas Wenzlaff</span></div>
</header>
<nav class="abs nav">
  <a href="#">HAUPTSEITE</a><a href="#">PRAXIS</a><a href="#">TEAM</a><a href="#">SPRECHZEITEN</a><a href="#">LEISTUNGEN</a><a href="#">KONTAKT</a>
</nav>
<div class="abs hero" role="img" aria-label="Photo of a long-haired dog resting on a treatment table"></div>

<section>
  <p class="abs welcome-kicker">Welcome to our website</p>
  <h1 class="abs welcome-title">Dr. med. Jonas Wenzlaff Vet Clinic &amp; Services</h1>
  <p class="abs welcome-text">Welcome to the veterinary practice of Dr. med. Jonas Wenzlaff. My team and I have put together information about the practice and information for patients. The traditional role of a health care provider in a community is to provide easy access to quality care. This is our main mission. It is very Important. We are focused on getting an animal and its owner in front of a veterinarian as soon as possible.</p>
  <div class="abs pets-photo" role="img" aria-label="Photo of a kitten and a small terrier with a stethoscope"></div>
</section>

<section>
  <div class="abs praxis-back"></div>
  <div class="abs praxis-panel"></div>
  <div class="abs praxis-photo one" role="img" aria-label="Photo of the practice building among trees"></div>
  <div class="abs praxis-photo two" role="img" aria-label="Photo of the practice entrance"></div>
  <p class="abs praxis-label">Praxis</p>
  <p class="abs praxis-text">Ich habe die Praxis <span class="year">1985</span> gegründet. Die Praxisräume befanden sich zuerst in der Lindenhofweg 1. 1995 sind wir in die jetzigen, grösseren Räume in der Lindenhofweg 4 umgezogen.</p>
  <a class="abs read-more" href="#" style="left:646px;top:1366px">Read More</a>
</section>

<section>
  <div class="abs services-bg"></div>
  <h2 class="abs team-title">Team</h2>
  <p class="abs team-text">Das Praxisteam besteht aus einer angestellten Tierärztin, einem angestellten Tierarzt, mehreren tiermedizinischen Fachangestellten und Auszubildenden sowie mir. Wir arbeiten als Team und tun alles um als fachkundige Partner des Tierhalters eine weitgehende Gesundheit der gehaltenen Tiere und ein zufriedenes Zusammenleben zwischen Mensch und Tier zu erreichen.</p>
  <a class="abs read-more" href="#" style="left:182px;top:1734px">Read More</a>
  <svg class="abs" style="left:782px;top:1608px" width="16" height="24" viewBox="0 0 16 24"><path d="M12 3 4 12l8 9" fill="none" stroke="#222" stroke-width="2"/></svg>
  <div class="abs portrait a" role="img" aria-label="Portrait of the practice veterinarian"></div>
  <div class="abs portrait b" role="img" aria-label="Portrait of the associate veterinarian"></div>
  <svg class="abs" style="left:1090px;top:1608px" width="16" height="24" viewBox="0 0 16 24"><path d="M4 3l8 9-8 9" fill="none" stroke="#222" stroke-width="2"/></svg>
</section>

<section>
  <div class="abs services-photo" role="img" aria-label="Photo of a dachshund and a black and white cat"></div>
  <h2 class="abs services-title">Leistungen</h2>
  <span class="abs service" style="left:610px;top:1908px">DOGS</span>
  <span class="abs service" style="left:610px;top:1938px">CATS</span>
  <span class="abs service" style="left:610px;top:1970px">SMALL PETS/ SMALL MAMMALS</span>
  <span class="abs service" style="left:922px;top:1908px">FOCUS</span>
  <span class="abs service" style="left:922px;top:1938px">SPECIAL SERVICES</span>
  <span class="abs service" style="left:922px;top:1970px">MEDICAL INSTITUTIONS</span>
  <a class="abs btn" href="#" style="left:610px;top:2022px;width:130px;height:38px">Read More</a>
</section>

<section>
  <div class="abs map" role="img" aria-label="Street map showing the location of the practice"></div>
  <div class="abs vet-photo" role="img" aria-label="Photo of a veterinarian trimming a cat's claws"></div>
</section>

<section>
  <h3 class="abs contact-name">Dr. med. vet. Jonas</h3>
  <p class="abs contact-line" style="top:2684px">Fachtierarzt für Kleintiere Lindenhofweg 4</p>
  <p class="abs contact-line" style="top:2714px">14169 Berlin (Dahlem)</p>
  <p class="abs contact-line" style="top:2750px">Telefon: 030 / 555 01 23</p>
  <p class="abs contact-line" style="top:2774px">Telefax: 030 / 555 01 24</p>
  <a class="abs btn" href="#" style="left:100px;top:2822px;width:166px;height:38px;font-size:12px;letter-spacing:1px">CONTACT US</a>

  <h3 class="abs hours-title">Sprechzeiten ohne Terminvereinbarung</h3>
  <table class="abs hours">
    <tr><td>Montag</td><td>9:30 - 11:00</td><td>16:00 - 19:00</td></tr>
    <tr><td>Dienstag</td><td>9:30 - 11:00</td><td>16:00 - 19:00</td></tr>
    <tr><td>Mittwoch</td><td>9:30 - 11:00</td><td>16:00 - 19:00</td></tr>
    <tr><td>Donnerstag</td><td>16:00 - 19:00</td><td></td></tr>
    <tr><td>Freitag</td><td>9:30 - 11:00</td><td>16:00 - 19:00</td></tr>
    <tr><td>Samstag</td><td>9:30 - 11:00</td><td></td></tr>
  </table>
</section>

<footer class="abs footer">DR-WENZLAFF.DE© 2018. ALL RIGHTS RESERVED</footer>
</body>
</html>
```